Australian tool shop needs a label designed for a new product

we need a label designed for a new product (Trowel Mate) but since its new to the market we want the label to be based on the design of the top 2 existing brands so it is instantly familiar with the customer, attached a photo of the 2 different brands that it needs to look like

Target Market(s)

BRICKLAYERS/ BUILDERS

Industry/Entity Type

Building Product

Requirements
Must have
• MUST HAVE SIMULAR FEELS AS THE UPLOADED IMAGE AND FEEL FAMILIAR WITH THOSE BRANDS

```html
<!DOCTYPE html>
<html lang="en">
<head>
<meta charset="utf-8">
<title>Trowel Mate – 20kg Bag Label</title>
<link rel="stylesheet" href="https://fonts.googleapis.com/css2?family=Anton&family=Roboto+Condensed:wght@400;700&display=swap">
<style>
  :root {
    --label-blue: #7bbcdd;
    --label-blue-deep: #67a9cf;
    --label-blue-soft: #a9d2e8;
    --ink-blue: #0c62a6;
    --paper: #ffffff;
    --page: #ffffff;
    --copy-light: #eef4f8;
  }
  html, body {
    margin: 0;
    padding: 0;
    width: 1137px;
    height: 1200px;
    overflow: hidden;
    background: var(--page);
  }
  .label {
    position: relative;
    width: 1137px;
    height: 1200px;
    overflow: hidden;
    background: var(--label-blue);
    font-family: "Roboto Condensed", Arial, sans-serif;
  }
  .label__shapes {
    position: absolute;
    inset: 0;
  }
  .brand-title {
    position: absolute;
    left: 100px;
    top: 50px;
    margin: 0;
    font-family: "Anton", Impact, sans-serif;
    font-weight: 400;
    font-size: 178px;
    line-height: 168px;
    letter-spacing: 1px;
    color: var(--ink-blue);
    text-transform: uppercase;
  }
  .net-weight {
    position: absolute;
    left: 852px;
    top: 102px;
    width: 186px;
    text-align: center;
    color: var(--ink-blue);
    line-height: 1;
  }
  .net-weight__amount {
    display: block;
    font-family: "Anton", Impact, sans-serif;
    font-size: 62px;
  }
  .net-weight__unit {
    display: block;
    font-size: 48px;
    margin-top: -2px;
  }
  .benefits {
    position: absolute;
    left: 105px;
    top: 470px;
    margin: 0;
    padding: 0;
    list-style: none;
    color: var(--copy-light);
    font-size: 37px;
    line-height: 43px;
  }
  .pack-count {
    position: absolute;
    left: 550px;
    top: 925px;
    width: 540px;
    margin: 0;
    text-align: center;
    font-weight: 700;
    font-size: 50px;
    line-height: 60px;
    color: var(--ink-blue);
    transform: rotate(-13deg);
    transform-origin: center;
    white-space: nowrap;
  }
  .usage-icons {
    position: absolute;
    left: 72px;
    top: 1104px;
    display: flex;
    gap: 48px;
  }
  .usage-icons__item {
    width: 90px;
    height: 90px;
    border-radius: 50%;
    background: var(--ink-blue);
  }
  .other-uses {
    position: absolute;
    right: 58px;
    top: 1118px;
    margin: 0;
    text-align: right;
    color: var(--ink-blue);
    font-size: 33px;
    line-height: 40px;
  }
  .other-uses strong {
    font-weight: 700;
  }
</style>
</head>
<body>
  <main class="label">
    <svg class="label__shapes" width="1137" height="1200" viewBox="0 0 1137 1200">
      <defs>
        <linearGradient id="tool-area-fill" x1="0" y1="0" x2="1" y2="1">
          <stop offset="0" stop-color="#f4f9fc"/>
          <stop offset="1" stop-color="#d6eaf5"/>
        </linearGradient>
      </defs>
      <path fill="var(--label-blue-soft)" d="M700 0 H1137 V420 C1040 400 960 420 900 440 C820 470 760 420 730 330 C700 240 740 180 700 0 Z"/>
      <path fill="var(--paper)" d="M0 0 H745 C700 60 720 130 760 210 C800 300 760 360 700 385 C640 410 560 430 470 410 C340 380 160 380 0 450 Z"/>
      <path fill="var(--paper)" d="M860 150 C860 95 920 70 985 72 C1050 74 1085 110 1080 160 C1075 210 1030 238 960 235 C895 232 860 200 860 150 Z"/>
      <path fill="var(--label-blue-soft)" d="M0 1000 C160 990 300 1050 430 1060 C560 1070 640 1030 780 1040 C900 1050 980 1110 1137 1090 V1200 H0 Z"/>
      <path fill="var(--paper)" d="M0 1110 C200 1080 360 1130 520 1120 C660 1110 700 1070 800 1080 C900 1090 1000 1100 1137 1080 V1200 H0 Z"/>
      <rect class="tool-area" role="img" aria-label="Bricklayer's trowel illustration" x="450" y="595" width="687" height="470" fill="url(#tool-area-fill)"/>
    </svg>

    <h1 class="brand-title">Trowel<br>Mate</h1>

    <div class="net-weight">
      <span class="net-weight__amount">20kg</span>
      <span class="net-weight__unit">net</span>
    </div>

    <ul class="benefits">
      <li>Blend with sand &amp; cement for mortar</li>
      <li>Enchances mortar bond strength &amp; workability</li>
    </ul>

    <p class="pack-count">50 Bags = 1 Tonne net</p>

    <div class="usage-icons">
      <div class="usage-icons__item" role="img" aria-label="Two-person lift safety pictogram"></div>
      <div class="usage-icons__item" role="img" aria-label="Bricklaying with trowel pictogram"></div>
      <div class="usage-icons__item" role="img" aria-label="Soil and slope treatment pictogram"></div>
    </div>

    <p class="other-uses"><strong>plus</strong> water treatment,<br>sanistising &amp; many other uses</p>
  </main>
</body>
</html>
```